Email Signatures

I would like to create a new email signature for my team. The design will be the same for everyone, with only individual details such as name and email changing. You can also see our brand style on our website. https://www.tlmbespokehomes.com.au/

Target Market(s)

Clients for new builds or renovations

Industry/Entity Type

Construction

Colors

Designer to choose colors to be used in the design.

```html
<!DOCTYPE html>
<html lang="en">
<head>
<meta charset="utf-8">
<title>TLM Bespoke Homes – Email Signature</title>
<link rel="stylesheet" href="https://fonts.googleapis.com/css2?family=Heebo:wght@500&family=Saira:wght@500;600;700&display=swap">
<style>
  :root {
    --page-bg: #e9e6e2;
    --card-bg: #221f20;
    --brand-green: #2c9b45;
    --icon-green: #0f8a3c;
    --text-white: #f3f3f3;
    --rule: #3b3839;
  }
  html, body {
    margin: 0;
    width: 1200px;
    height: 1200px;
    overflow: hidden;
    background: var(--page-bg);
  }
  .signature {
    position: absolute;
    left: 50px;
    top: 112px;
    width: 1100px;
    height: 976px;
    background: var(--card-bg);
    font-family: "Saira", sans-serif;
    color: var(--text-white);
  }
  .brand {
    position: absolute;
    left: 44px;
    top: 140px;
    display: flex;
    align-items: center;
    gap: 22px;
  }
  .brand-mark {
    width: 56px;
    height: 56px;
    background: var(--brand-green);
  }
  .brand-name {
    font-family: "Saira", sans-serif;
    font-weight: 700;
    font-size: 58px;
    line-height: 1;
    color: var(--text-white);
    white-space: nowrap;
  }
  .person {
    position: absolute;
    left: 44px;
    top: 376px;
    white-space: nowrap;
  }
  .person-name {
    font-family: "Heebo", sans-serif;
    font-weight: 500;
    font-size: 46px;
    color: var(--brand-green);
  }
  .person-role {
    font-weight: 600;
    font-size: 30px;
    margin-left: 10px;
  }
  .rule {
    position: absolute;
    left: 44px;
    width: 816px;
    height: 1px;
    background: var(--rule);
  }
  .rule-top { top: 485px; }
  .rule-bottom { top: 816px; }
  .contact {
    position: absolute;
    left: 44px;
    margin: 0;
    font-size: 30px;
    font-weight: 600;
    line-height: 1;
    white-space: nowrap;
  }
  .contact-label {
    display: inline-block;
    width: 52px;
    font-weight: 500;
    color: var(--icon-green);
  }
  .social {
    position: absolute;
    top: 857px;
    display: flex;
    align-items: center;
    gap: 12px;
    font-size: 28px;
    font-weight: 600;
    white-space: nowrap;
  }
  .social-dot {
    width: 44px;
    height: 44px;
    border: 1.5px solid var(--icon-green);
    border-radius: 50%;
    box-sizing: border-box;
  }
  .social-divider {
    position: absolute;
    top: 862px;
    width: 1px;
    height: 38px;
    background: #2b2829;
  }
</style>
</head>
<body>
  <div class="signature">
    <div class="brand">
      <span class="brand-mark"></span>
      <span class="brand-name">TLM Bespoke Homes</span>
    </div>

    <div class="person">
      <span class="person-name">Liam Hartley,</span><span class="person-role">General Manager</span>
    </div>

    <div class="rule rule-top"></div>

    <p class="contact" style="top:526px"><span class="contact-label">M:</span>0400 123 456</p>
    <p class="contact" style="top:598px"><span class="contact-label">E:</span>info@tlmbespokehomes.com.au</p>
    <p class="contact" style="top:670px"><span class="contact-label">A:</span>Kingsford, Tasmania Australia</p>
    <p class="contact" style="top:743px"><span class="contact-label">W.</span>www.tlmbespokehomes.com.au</p>

    <div class="rule rule-bottom"></div>

    <div class="social" style="left:44px"><span class="social-dot"></span>Plusline</div>
    <div class="social-divider" style="left:251px"></div>
    <div class="social" style="left:273px"><span class="social-dot"></span>Linkwise</div>
    <div class="social-divider" style="left:487px"></div>
    <div class="social" style="left:523px"><span class="social-dot"></span>Circlebook</div>
    <div class="social-divider" style="left:725px"></div>
    <div class="social" style="left:762px"><span class="social-dot"></span>Snapgram</div>
  </div>
</body>
</html>
```